Dozing Heron

Need a business card for our restaurant. Restaurant and Bar in the mountains of North Idaho. Rustic looking card

Contact Information for Business Card

rustic design, wood and metal looking, primarily neutral colors

Requirements
Must have
• Name, address, phone number, website, email address

```html
<!DOCTYPE html>
<html lang="en">
<head>
<meta charset="utf-8">
<title>The Dozing Heron – Business Card</title>
<link href="https://fonts.googleapis.com/css2?family=Catamaran:wght@400;500;700;800&display=swap" rel="stylesheet">
<style>
  :root {
    --backdrop: #8b8c8f;
    --card-dark: #222223;
    --mark-dark: #3a3a3c;
    --card-light: #ffffff;
    --ink: #111111;
    --band: #0c0c0c;
    --band-text: #ffffff;
  }
  * { margin: 0; padding: 0; box-sizing: border-box; }
  html, body { width: 900px; height: 1200px; overflow: hidden; }
  body {
    background: var(--backdrop);
    font-family: "Catamaran", sans-serif;
    position: relative;
  }
  .card {
    position: absolute;
    left: 135px;
    width: 631px;
    height: 357px;
    border-radius: 12px;
    overflow: hidden;
  }
  .card--front { top: 216px; background: var(--card-dark); }
  .card--back { top: 629px; background: var(--card-light); color: var(--ink); }

  .seal {
    position: absolute;
    border-radius: 50%;
    display: flex;
    align-items: center;
    justify-content: center;
    text-align: center;
    font-weight: 700;
    text-transform: uppercase;
    letter-spacing: 2px;
    line-height: 1.15;
  }
  .card--front .seal {
    left: 184px; top: 47px; width: 262px; height: 262px;
    border: 3px solid var(--mark-dark);
    color: var(--mark-dark);
    font-size: 26px;
  }
  .card--back .seal {
    left: 61px; top: 77px; width: 222px; height: 222px;
    border: 6px solid var(--ink);
    color: var(--ink);
    font-size: 22px;
  }

  .contact { position: absolute; left: 301px; top: 60px; }
  .contact__name { font-size: 24px; font-weight: 800; letter-spacing: 1px; line-height: 1; }
  .contact__role { font-size: 14px; font-weight: 500; margin-top: 6px; }
  .contact__address { font-size: 14.5px; line-height: 23px; margin-top: 40px; letter-spacing: .3px; }
  .contact__list { list-style: none; margin-top: 14px; }
  .contact__list li {
    display: flex; align-items: center; gap: 6px;
    font-size: 14.5px; height: 29px; letter-spacing: .3px;
  }
  .contact__list .phone { letter-spacing: 2.5px; }
  .contact__list svg { width: 15px; height: 15px; flex: none; }

  .services {
    position: absolute; left: 0; right: 0; top: 307px; height: 32px;
    background: var(--band);
    color: var(--band-text);
    font-weight: 700; font-size: 16px; letter-spacing: .4px;
  }
  .services span { position: absolute; top: 5px; transform: translateX(-50%); white-space: nowrap; }
</style>
</head>
<body>

  <section class="card card--front" aria-label="Card front">
    <div class="seal">The<br>Dozing<br>Heron</div>
  </section>

  <section class="card card--back" aria-label="Card back">
    <div class="seal">The<br>Dozing<br>Heron</div>

    <div class="contact">
      <h1 class="contact__name">MARTIN HALE</h1>
      <p class="contact__role">Founder</p>
      <p class="contact__address">214 Ridge St,<br>Pinecrest, ID 83800</p>
      <ul class="contact__list">
        <li class="phone">
          <svg viewBox="0 0 24 24" aria-hidden="true"><path fill="#111" d="M6.6 10.8a15.1 15.1 0 0 0 6.6 6.6l2.2-2.2c.3-.3.7-.4 1-.2 1.1.4 2.3.6 3.6.6.6 0 1 .4 1 1V20c0 .6-.4 1-1 1A17 17 0 0 1 3 4c0-.6.4-1 1-1h3.5c.6 0 1 .4 1 1 0 1.3.2 2.5.6 3.6.1.3 0 .7-.2 1z"/></svg>
          (208) 555-0143
        </li>
        <li>
          <svg viewBox="0 0 24 24" aria-hidden="true"><path fill="#111" d="M2 5h20v14H2z"/><path fill="none" stroke="#fff" stroke-width="1.6" d="M2.5 5.5 12 13l9.5-7.5"/></svg>
          info@thedozingheronpinecrest.com
        </li>
        <li>
          <svg viewBox="0 0 24 24" aria-hidden="true"><g fill="none" stroke="#111" stroke-width="1.8"><circle cx="12" cy="12" r="9.5"/><ellipse cx="12" cy="12" rx="4" ry="9.5"/><path d="M2.5 12h19M4 7h16M4 17h16"/></g></svg>
          thedozingheronpinecrest.com
        </li>
      </ul>
    </div>

    <div class="services">
      <span style="left:79px">Dine-in</span>
      <span style="left:172px">-</span>
      <span style="left:294px">Outdoor seating</span>
      <span style="left:405px">-</span>
      <span style="left:519px">In-store pickup</span>
    </div>
  </section>

</body>
</html>
```